Stationery Design Project

We need a stationery design to change our look to a more corporate design. My company has been established since 1989 and over that time has changed from your average sign company to doing more Corporate re branding projects and have some multi National clients.
Our website is currently being redesigned so we need a new logo and business cards etc. to compliment it.
I have 2 graphic designers employed but i want on outsiders opinion and a totally independant view point.
Updates
Hi Designers
We are predominantely a sign manufacturing company that manufacturers every type of sign you can imagine. However the majoprity of our work is digital graphics. Our claim to faim is that we wrap the Harbour Skytrams and Glidetrams which everyone seems to know in Sydney.We also do all sorts of Large format digital printing, vehicle wraps,vinyl signage,LED & Neon Illuminated signage,CNC Routing all materials,Laser cutting and Engraving, Architectural signage, Cut Out letters and Screenprinting.
Aswell as this we totally re-brand companies with internal wall graphics reception signage way finding signage and the like.We are a medium size company that has been trading since 1989 and has some very large reputable clients.
Our Company name is Brightmark Pty Ltd but like to have Signage and Graphics in our stationery.
Our details are as follows T: 9381 5027 F: 9381 5063 Unit 4, 22 Quarry Lane.Pine Flats. NSW 2163 email mail@brightmarkexample.com our current website is being re-designed www.brightmarkexample.com
The design and colour scheme i would like is quite simple with a corporate feel and blue, grey & magenta are colours that seem to suit but am open to most suggestions just looking for clean lines.
Hopefully this is enough information if you require any more please ask.
Regards Neil Barrowby
We are looking to simplify our LOGO not too concerned yet about layout of stationery items that we can easily work on later. I want to get a new logo that we can work with before we return to work on the 16th January so please concentrate on just the logo for now.
We would like to have Signs & Graphics somewhere in the name even though our registered name is Brightmark Pty Ltd. Brightmark is one word, i want it to be quite a bold font with no seriffs.The bright blue and grey colours are favourites so far with maybe a little magenta added later. Would like to have a Logo that is totally seperate and then the Brightmark P/L Signs & graphics as a secondary item just to let people know what Brightmark do as the name obviously does not say what we are about.
Also we need to consider how we can put logo on T-shirts work shirts and company vehicles.
We do not need CD cover or envelopes but letterheads and business cards.
Industry/Entity Type
Business
Look and feel
Each slider illustrates characteristics of the customer's brand and the style your logo design should communicate.

```html
<!DOCTYPE html>
<html lang="en">
<head>
<meta charset="utf-8">
<title>Brightmark business cards</title>
<link href="https://fonts.googleapis.com/css2?family=Crimson+Text:wght@400&family=Source+Sans+3:wght@400;600&display=swap" rel="stylesheet">
<style>
  :root {
    --stage: #1b1b1b;
    --grey: #676767;
    --grey-dark: #5e5e5e;
    --white: #ffffff;
    --paper-end: #e9e9e9;
    --magenta: #ec0c83;
    --magenta-soft: #f25aa6;
    --blue: #0a85b2;
    --blue-light: #4ab4d3;
    --ink: #3a3a3a;
    --muted: #6b6b6b;
  }
  * { margin: 0; padding: 0; box-sizing: border-box; }
  html, body { width: 1200px; height: 960px; overflow: hidden; background: var(--stage); }
  .canvas { position: relative; width: 1200px; height: 960px; }

  .card {
    position: absolute;
    left: 283px;
    width: 634px;
    height: 362px;
    border-radius: 22px;
    overflow: hidden;
  }
  .card--back { top: 92px; background: var(--grey); }
  .card--front { top: 482px; background: linear-gradient(180deg, var(--white) 45%, var(--paper-end) 100%); }
  .card__art { position: absolute; inset: 0; width: 634px; height: 362px; }

  .brand { position: absolute; display: flex; align-items: center; }
  .brand__dot {
    width: 80px; height: 80px; border-radius: 50%;
    background: var(--blue);
    flex: none;
  }
  .brand__text { margin-left: 22px; }
  .brand__name {
    font-family: "Crimson Text", Georgia, serif;
    font-weight: 400;
    font-size: 46px;
    line-height: 1;
    display: block;
  }
  .brand__tag {
    font-family: "Source Sans 3", Arial, sans-serif;
    font-weight: 600;
    font-size: 12px;
    letter-spacing: 7.4px;
    color: var(--blue);
    display: block;
    margin-top: 4px;
    padding-left: 3px;
  }
  .card--back .brand { left: 297px; top: 253px; }
  .card--back .brand__name { color: var(--white); }
  .card--back .brand__tag { color: var(--blue); opacity: .75; }
  .card--front .brand { left: 29px; top: 27px; }
  .card--front .brand__dot { margin-right: 0; }
  .card--front .brand__name { color: #111; }

  .contact {
    position: absolute; left: 36px; top: 146px;
    font-family: "Source Sans 3", Arial, sans-serif;
    color: var(--ink);
  }
  .contact__name { font-size: 23px; font-weight: 600; color: var(--blue); line-height: 1.1; }
  .contact__role { font-size: 16px; color: var(--muted); margin-top: 2px; }
  .contact__address { font-size: 16px; line-height: 21px; margin-top: 17px; }
  .contact__list { list-style: none; margin-top: 6px; font-size: 16px; }
  .contact__list li { display: flex; align-items: center; height: 22.5px; }
  .contact__icon { width: 14px; height: 14px; margin-right: 14px; flex: none; }
</style>
</head>
<body>
<main class="canvas">

  <section class="card card--back" aria-label="Card back">
    <svg class="card__art" viewBox="0 0 634 362" aria-hidden="true">
      <defs>
        <linearGradient id="back-swirl" x1="0" y1="0" x2="1" y2="1">
          <stop offset="0" stop-color="#ef2a90"/>
          <stop offset=".45" stop-color="#3aa6c8"/>
          <stop offset="1" stop-color="#0a85b2"/>
        </linearGradient>
      </defs>
      <circle cx="80" cy="172" r="208" fill="#ffffff"/>
      <circle cx="80" cy="172" r="192" fill="#666666"/>
      <circle cx="80" cy="172" r="178" fill="#ffffff"/>
      <circle cx="80" cy="172" r="165" fill="url(#back-swirl)" role="img" aria-label="Large brand colour field in magenta and blue"/>
    </svg>
    <div class="brand">
      <span class="brand__dot"></span>
      <span class="brand__text">
        <span class="brand__name">Brightmark</span>
        <span class="brand__tag">SIGN TECHNOLOGY</span>
      </span>
    </div>
  </section>

  <section class="card card--front" aria-label="Card front">
    <svg class="card__art" viewBox="0 0 634 362" aria-hidden="true">
      <defs>
        <linearGradient id="front-swirl" x1="0" y1="0" x2="1" y2="1">
          <stop offset="0" stop-color="#f25aa6"/>
          <stop offset=".5" stop-color="#ec0c83"/>
          <stop offset=".75" stop-color="#2aa9c8"/>
          <stop offset="1" stop-color="#0a85b2"/>
        </linearGradient>
      </defs>
      <circle cx="507" cy="198" r="194" fill="#666666"/>
      <circle cx="507" cy="198" r="178" fill="#ffffff"/>
      <circle cx="507" cy="198" r="155" fill="url(#front-swirl)" role="img" aria-label="Large brand colour field in magenta and blue"/>
    </svg>

    <div class="brand">
      <span class="brand__dot"></span>
      <span class="brand__text">
        <span class="brand__name">Brightmark</span>
        <span class="brand__tag">SIGN TECHNOLOGY</span>
      </span>
    </div>

    <div class="contact">
      <p class="contact__name">Colin Ashdown</p>
      <p class="contact__role">Marketing Manager</p>
      <p class="contact__address">22 Quarry Lane<br>Pine Flats. NSW 2163</p>
      <ul class="contact__list">
        <li>
          <svg class="contact__icon" viewBox="0 0 14 14" aria-hidden="true"><path d="M1 5c0-2 2-3 6-3s6 1 6 3l-3 1-1-1.5H5L4 6z M3 7h8l1 5H2z" fill="#0a85b2"/></svg>
          9381 5027
        </li>
        <li>
          <svg class="contact__icon" viewBox="0 0 14 14" aria-hidden="true"><rect x="3" y="1" width="8" height="4" fill="none" stroke="#0a85b2" stroke-width="1.2"/><rect x="1" y="5" width="12" height="5" fill="#0a85b2"/><rect x="3" y="9" width="8" height="4" fill="#fff" stroke="#0a85b2" stroke-width="1.2"/></svg>
          9381 5063 Unit 4
        </li>
        <li>
          <svg class="contact__icon" viewBox="0 0 14 14" aria-hidden="true"><rect x="1" y="3" width="12" height="8" fill="none" stroke="#0a85b2" stroke-width="1.4"/><path d="M1 3l6 5 6-5" fill="none" stroke="#0a85b2" stroke-width="1.4"/></svg>
          colin@brightmarkexample.com
        </li>
        <li>
          <svg class="contact__icon" viewBox="0 0 14 14" aria-hidden="true"><circle cx="7" cy="7" r="6" fill="none" stroke="#0a85b2" stroke-width="1.3"/><ellipse cx="7" cy="7" rx="2.6" ry="6" fill="none" stroke="#0a85b2" stroke-width="1.1"/><path d="M1 7h12" stroke="#0a85b2" stroke-width="1.1"/></svg>
          www.brightmarkexample.com
        </li>
      </ul>
    </div>
  </section>

</main>
</body>
</html>
```